Restaurant Poster Design Project for A-Frame

I am after a poster, which will go on an outdoor A-Frame (A1 size - this size is to be confirmed) outlining our drink/happy hour/specials for our Mexican Restaurant and Bar.

Specific details are:

$4 Beer, Wine and Spirits
$5 Margaritas
everynight 5:30pm-7:30pm

I will supply logo, which needs to be incorporated (really small) into the poster, along with our address: 42 Lowden Road, Windsor - (Im not too sure if we should include our phone number or not ?? Please advise what you feel will look good etc

Happy for you to add a phrase or wording etc, as long as the specific details are included, above.

We also have an enclosed beer garden in the rear of the restaurant - Do you believe I should mention this?

I am really open to eye catching designs and ALL suggestions welcome please!
Updates

Please find attached of samples that I am sort of after: (please let me know if they cant be opened).

http://www.flyerquill.example/blog/wp-content/uploads/2012/06/happyHourPoster-e1340372894746.gif

http://marekvu.files.samplepress.example/2012/10/profolio_0012.jpg?w=1169

http://3.img.noteleaf.example/-NfNjpdG5w/T5pohPd0AhI/AAAAAAAADRs/CA7DPeI_PyU/s640/vintage_poster.jpg

http://www.orchidvane.example/files/imagecache/Event/news/teaser/Lounge_Happy_Hour_Poster_-_Mar_2011_bilingual.jpg

http://www.tkrumps.example/dallas/images/happyhour_poster.jpg

http://cdn2-b.newsgrove.example/sites/default/files/styles/large_lightbox/hash/9a/d1/9ad11350ba178511886fddcff7aaac8d.jpg?itok=wDl2vlfJ

http://www.platterpicks.example/imageservice/images/13/1313171414293_244/img_large_watermarked.jpg

Target Market(s)

18 YEARS OLD AND OVER

Industry/Entity Type

Restaurant

Requirements
Must have
• Address
Phone Number
Logo
Clear easy to read font, to be seen via cars + ppl walking down street
If images are included, to be clear and visable
Nice to have
• Images are possible
To mention a beer garden
Should not have
• Traditional Mexican Colourful 80's Theme

```html
<!DOCTYPE html>
<html lang="en">
<head>
<meta charset="utf-8">
<title>Happy Hour – Pardo Taqueria</title>
<link rel="stylesheet" href="https://fonts.googleapis.com/css2?family=Arimo:ital,wght@0,400;0,700;1,700&family=Montserrat:wght@600;700&family=Roboto+Condensed:wght@400;700&display=swap">
<style>
  :root {
    --paper: #ffffff;
    --ink: #111111;
    --lime: #3aa637;
    --lime-deep: #1f6e1c;
    --bottle-dark: #0e3a12;
    --bottle-mid: #2f8a2c;
    --bottle-light: #8fd46a;
    --panel: rgba(100,100,100,.9);
    --grey-text: #707070;
    --white: #ffffff;
  }
  * { margin: 0; padding: 0; box-sizing: border-box; }
  html, body { width: 835px; height: 1200px; overflow: hidden; background: var(--paper); }
  .poster {
    position: relative;
    width: 835px;
    height: 1200px;
    background: var(--paper);
    overflow: hidden;
    font-family: "Arimo", Arial, sans-serif;
  }
  .bottle-photo {
    position: absolute;
    inset: 0;
    background:
      radial-gradient(ellipse 120px 380px at 740px 260px, rgba(190,240,150,.55), transparent 70%),
      radial-gradient(ellipse 220px 200px at 640px 1050px, rgba(140,220,100,.5), transparent 70%),
      linear-gradient(110deg, var(--bottle-dark) 0%, var(--bottle-mid) 50%, var(--bottle-light) 72%, var(--bottle-mid) 86%, var(--bottle-dark) 100%);
    clip-path: polygon(640px 0, 835px 0, 835px 1200px, 505px 1200px, 515px 900px, 545px 620px, 600px 420px, 630px 250px);
  }
  .headline-favorites {
    position: absolute;
    left: 12px;
    top: 40px;
    color: var(--lime);
    font-family: "Montserrat", Arial, sans-serif;
    font-weight: 600;
    line-height: 1;
  }
  .headline-favorites .line-small { display: block; font-size: 78px; letter-spacing: -1px; }
  .headline-favorites .line-large { display: block; font-size: 112px; font-weight: 700; letter-spacing: -3px; margin-top: -8px; }
  .price-band {
    position: absolute;
    left: 0;
    top: 252px;
    width: 760px;
    height: 60px;
    background: var(--ink);
    color: var(--white);
    font-size: 40px;
    line-height: 60px;
    padding-left: 10px;
    white-space: nowrap;
  }
  .price-band .price { color: var(--lime); font-weight: 700; }
  .price-band .gap { display: inline-block; width: 22px; }
  .schedule {
    position: absolute;
    left: 10px;
    top: 322px;
    font-family: "Roboto Condensed", Arial, sans-serif;
    font-weight: 700;
    font-size: 46px;
    color: var(--grey-text);
    letter-spacing: 0.5px;
  }
  .happy-hour {
    position: absolute;
    left: 237px;
    top: 515px;
    width: 448px;
    height: 390px;
    background: var(--panel);
    color: var(--white);
    font-family: "Roboto Condensed", Arial, sans-serif;
    font-weight: 400;
    font-size: 152px;
    line-height: 150px;
    padding: 48px 0 0 16px;
    letter-spacing: -2px;
  }
  .beer-garden {
    position: absolute;
    left: 180px;
    top: 988px;
    width: 376px;
    text-align: right;
    font-size: 25px;
    line-height: 1.25;
    color: var(--ink);
  }
  .beer-garden em { color: var(--lime); font-weight: 700; font-style: italic; }
  .brand {
    position: absolute;
    left: 10px;
    top: 1120px;
    display: flex;
    align-items: center;
    gap: 6px;
    font-family: "Arimo", Arial, sans-serif;
    font-weight: 700;
    font-size: 19px;
    color: var(--lime-deep);
    line-height: 1.05;
  }
  .brand .dot { width: 16px; height: 16px; border-radius: 50%; background: var(--lime-deep); flex: none; }
  .brand .name { width: 118px; }
  .address-bar {
    position: absolute;
    left: 158px;
    top: 1112px;
    width: 677px;
    height: 60px;
    background: var(--ink);
    color: var(--white);
    font-size: 29px;
    font-weight: 700;
    line-height: 60px;
    padding-left: 14px;
    white-space: nowrap;
  }
</style>
</head>
<body>
  <main class="poster">
    <div class="bottle-photo" role="img" aria-label="Close-up photo of a chilled green beer bottle covered in condensation droplets"></div>

    <h1 class="headline-favorites">
      <span class="line-small">favorites</span>
      <span class="line-large">served</span>
    </h1>

    <p class="price-band"><span class="price">$4</span> Beer, Wine &amp; Spirits<span class="gap"></span><span class="price">$5</span> Margarita</p>

    <p class="schedule">EVERY NIGHT 5.30PM-7.30PM</p>

    <h2 class="happy-hour">HAPPY<br>HOUR</h2>

    <p class="beer-garden">Have fun at our <em>enclosed<br>Beer Garden</em> in the rear<br>of the restaurant</p>

    <div class="brand"><span class="dot"></span><span class="name">Pardo Taqueria</span></div>

    <p class="address-bar">42 Lowden Road, Windsor. Ph.: 555 01 23 47</p>
  </main>
</body>
</html>
```